business card design for a small scale specialty cut flower farm

We need a business card design for Hollowmere Bloom Farm based in Langley, BC, Canada. We produce specialty, high-end cut flowers and sell locally to florists, local shops and markets and the end user through bouquet subscriptions. The final business card design should be memorable and have a timeless or vintage feel. We would prefer a square shape.
Updates

Target Market(s)

florists, shops and seasonal markets, local flower lovers

Industry/Entity Type

Floral

Contact Information for Business Card

Tamsin Ellery Voss, Grower
Langley, BC, Canada
website: hollowmerebloomfarm.example
instagram: @hollowmerebloomfarm
Tel: 555.317.4290
facebook: www.facebook.example/hollowmereblooms/

Font styles to use
Serif
Decorative
Script

Requirements
Must have
• soft black background colour on front side, the included logo and catch phrase: Fresh Local Seasonal
Nice to have
• phone number and website address on front of card, included photo 6539 incorporated onto the back, possibly photo 6609 as well.

```html
<!DOCTYPE html>
<html lang="en">
<head>
<meta charset="utf-8">
<title>Hollowmere Bloom Farm – Business Card</title>
<link rel="stylesheet" href="https://fonts.googleapis.com/css2?family=Montserrat:wght@400;500;700&display=swap">
<style>
  :root {
    --backdrop: #3a3a3a;
    --soft-black: #0b0b0b;
    --white: #ffffff;
    --pink: #e58bc6;
    --forest: #2c4a22;
    --lime: #b8e07a;
    --photo-garden-a: #9fc27a;
    --photo-garden-b: #e7b6c4;
    --photo-dahlia-a: #c0304a;
    --photo-dahlia-b: #7b5fc4;
  }
  * { box-sizing: border-box; margin: 0; padding: 0; }
  html, body { width: 1200px; height: 900px; overflow: hidden; }
  body {
    background: var(--backdrop);
    font-family: "Montserrat", Arial, sans-serif;
    position: relative;
  }
  .card {
    position: absolute;
    width: 520px;
    height: 300px;
    border-radius: 26px;
    overflow: hidden;
  }

  /* Front */
  .card-front {
    left: 50px; top: 300px;
    background: var(--soft-black);
    color: var(--white);
    display: flex;
    flex-direction: column;
    align-items: center;
    text-align: center;
  }
  .brand-dot {
    width: 30px; height: 30px;
    border-radius: 50%;
    background: var(--pink);
    margin-top: 56px;
  }
  .brand-name {
    margin-top: 18px;
    font-weight: 500;
    font-size: 27px;
    letter-spacing: 3px;
    text-transform: uppercase;
    line-height: 1.3;
    color: var(--white);
  }
  .catchphrase {
    margin-top: 22px;
    font-weight: 700;
    font-size: 15px;
    letter-spacing: 0.5px;
    color: var(--pink);
  }
  .contact-line {
    margin-top: 12px;
    font-weight: 500;
    font-size: 15px;
    letter-spacing: 0.3px;
  }

  /* Back */
  .card-back {
    left: 630px; top: 300px;
    background: var(--forest);
  }
  .photo {
    position: absolute;
    top: 0;
  }
  .photo-grower {
    left: 0; width: 252px; height: 206px;
    background: linear-gradient(160deg, var(--photo-garden-a) 0%, #6f9a4f 50%, var(--photo-garden-b) 100%);
    border-right: 4px solid var(--lime);
    border-bottom: 3px solid var(--lime);
  }
  .photo-dahlias {
    left: 252px; width: 268px; height: 170px;
    background: linear-gradient(135deg, var(--photo-dahlia-b) 0%, var(--photo-dahlia-a) 55%, #e26a78 100%);
    border-bottom: 3px solid var(--lime);
  }
  .owner {
    position: absolute;
    left: 0; right: 24px; top: 220px;
    text-align: right;
    color: var(--lime);
    font-size: 15px;
  }
  .owner-name { font-weight: 700; letter-spacing: 0.5px; }
  .owner-role { font-weight: 400; }
  .socials {
    position: absolute;
    left: 20px; right: 18px; bottom: 22px;
    display: flex;
    justify-content: space-between;
    color: var(--lime);
    font-size: 12.5px;
    font-weight: 500;
  }
  .social { display: flex; align-items: center; gap: 6px; }
  .social-dot {
    width: 16px; height: 16px;
    border-radius: 50%;
    border: 1.5px solid var(--lime);
  }
</style>
</head>
<body>
  <section class="card card-front" aria-label="Card front">
    <div class="brand-dot"></div>
    <h1 class="brand-name">Hollowmere<br>Bloom Farm</h1>
    <p class="catchphrase">FRESH LOCAL SEASONAL</p>
    <p class="contact-line">(555) 317-4290 | www.hollowmerebloomfarm.example</p>
  </section>

  <section class="card card-back" aria-label="Card back">
    <div class="photo photo-grower" role="img" aria-label="Photo of the grower holding a bucket of pink snapdragons in the flower field"></div>
    <div class="photo photo-dahlias" role="img" aria-label="Photo of a galvanised bucket full of red and pink dahlias"></div>
    <p class="owner"><span class="owner-name">TAMSIN ELLERY VOSS</span> <span class="owner-role">| OWNER</span></p>
    <div class="socials">
      <span class="social"><span class="social-dot"></span>@hollowmerebloomfarm</span>
      <span class="social"><span class="social-dot"></span>social.example/hollowmereblooms</span>
    </div>
  </section>
</body>
</html>
```